Brookvale Advisory Limited needs a Brochure/ Company Profile

We need a Company profile for our IT consulting company. We need to layout the brochure in a very unique and creative way that is captivating to any audience and fun to read. Our website gives a description of what we offer. www.brookvaleadvisory.example. The site also shows our color scheme. The Brochure will have the following main headings. (Please review the attachment for most of th content). Please note that these are the headings expected to be in each major section of the brochure so should form a table of content
1. Executive Summary
2. Philosophy
3. BAL Corporate Structure
4. BAL Capabilities
5. BAL Offerings
6. Industry Milestones
7. Management Team
8. Partners and Tools
This list is not exhaustive but should give a general idea of the direction.
Updates
Target Market(s)
Banking, Manufacturing, Small Businesses, Government
Industry/Entity Type
It Company
Requirements
Must have
- Size should be slightly smaller than A3 folded in halve. There should be a catchy professional looking frontpage and a simple backpage
Nice to have
- Networking Images, drawings, vector images /pictures that represent Information Technology, Networking, Computing, Unified Communications
Should not have
- The brochure must not contain any images from the website expect the company logo and must not have any pictures of individuals.
- There should not be any pictures copied from the website. Only images /picture that represent Information Technology, Networking, Computing, Unified Communications e.t.c should be in the brochure.

```html
<!DOCTYPE html>
<html lang="en">
<head>
<meta charset="utf-8">
<title>Brookvale Advisory Limited – Services</title>
<link href="https://fonts.googleapis.com/css2?family=Baloo+2:wght@600;700;800&family=Lilita+One&display=swap" rel="stylesheet">
<style>
  :root {
    --teal: #0f5d75;
    --orange: #e98a2c;
    --orange-deep: #d9741c;
    --white: #ffffff;
    --ink: #1f2a33;
  }
  * { margin: 0; padding: 0; box-sizing: border-box; }
  html, body { width: 848px; height: 1200px; overflow: hidden; background: var(--white); }
  .page {
    position: relative;
    width: 848px;
    height: 1200px;
    background: var(--teal);
    font-family: "Baloo 2", "Arial Rounded MT Bold", sans-serif;
    color: var(--white);
    overflow: hidden;
  }
  .page-header {
    position: absolute; left: 0; top: 0;
    width: 848px; height: 135px;
    background: var(--white);
  }
  .page-meta {
    position: absolute; left: 78px; top: 44px;
    font-size: 14px; font-weight: 700; color: var(--ink);
    letter-spacing: 0.2px;
  }
  .page-meta .divider { display: inline-block; margin: 0 6px; font-weight: 600; }
  .rule-orange {
    position: absolute; left: 0; top: 147px;
    width: 326px; height: 13px; background: var(--orange);
  }
  .rule-white {
    position: absolute; left: 332px; top: 147px;
    width: 516px; height: 13px; background: var(--white);
  }
  .service {
    position: absolute;
    text-align: center;
    transform: translateX(-50%);
    white-space: nowrap;
  }
  .service-number {
    display: block;
    font-family: "Lilita One", "Baloo 2", sans-serif;
    font-size: 30px;
    line-height: 1;
    color: var(--teal);
    -webkit-text-stroke: 2px var(--white);
    margin-bottom: 4px;
  }
  .service-title {
    font-size: 14px;
    font-weight: 800;
    color: var(--orange);
    line-height: 1.2;
    margin-bottom: 2px;
  }
  .service-list { list-style: none; }
  .service-list li {
    font-size: 12.5px;
    font-weight: 700;
    line-height: 17.6px;
  }
  .service--consultancy { left: 228px; top: 165px; }
  .service--audit { left: 615px; top: 165px; }
  .service--design { left: 227px; top: 758px; }
  .service--training { left: 612px; top: 758px; }
  .service--support { left: 435px; top: 890px; }

  .hero-art {
    position: absolute;
    left: 238px; top: 378px;
    width: 382px; height: 386px;
    border-radius: 50%;
    background: radial-gradient(circle at 50% 50%, var(--orange) 0 55%, var(--orange-deep) 56% 62%, rgba(255,255,255,0.0) 63%),
                radial-gradient(circle at 50% 50%, rgba(255,255,255,0.08) 0 70%, transparent 71%);
  }
</style>
</head>
<body>
<main class="page">
  <header class="page-header">
    <p class="page-meta">3<span class="divider">|</span>info@brookvaleadvisory.example</p>
  </header>
  <div class="rule-orange"></div>
  <div class="rule-white"></div>

  <section class="service service--consultancy">
    <span class="service-number">1</span>
    <h2 class="service-title">IT NETWORK CONSULTANCY AND ADVISORY</h2>
    <ul class="service-list">
      <li>Solution Requirements Definition</li>
      <li>Best Practice advisory</li>
      <li>IT Information Management</li>
      <li>Networking Systems Procurement</li>
      <li>IT Transformation</li>
      <li>IT Network Operations</li>
      <li>Managed Services</li>
      <li>Network Infrastructure Optimization</li>
    </ul>
  </section>

  <section class="service service--audit">
    <span class="service-number">2</span>
    <h2 class="service-title">INFRASTRUCTURE AUDIT</h2>
    <ul class="service-list">
      <li>GAP Analysis</li>
      <li>IT Network Security Audit</li>
      <li>Pre-system Implementation Review</li>
      <li>Post-System Implementation Review</li>
      <li>Enterprise Infrastructure Audit</li>
      <li>Technology assessment</li>
    </ul>
  </section>

  <div class="hero-art" role="img" aria-label="Flat illustration of a large orange circle surrounded by business icons: a price tag, a pencil, a gear, a thumbs-up, a magnifying glass and speech bubbles joined by dotted arrows"></div>

  <section class="service service--design">
    <span class="service-number">3</span>
    <h2 class="service-title">SOLUTION DESIGN</h2>
    <ul class="service-list">
      <li>Network Infrastructure Design</li>
      <li>Network Systems Architecture</li>
      <li>Network Systems Design Validation</li>
      <li>Data Center Network Infrastructure Design</li>
      <li>Unified Communications and Collaboration</li>
      <li>Network Virtualization Design</li>
    </ul>
  </section>

  <section class="service service--training">
    <span class="service-number">5</span>
    <h2 class="service-title">TRAINING</h2>
    <ul class="service-list">
      <li>Custom Built Infrastructure</li>
      <li>tailored training</li>
      <li>Industry certification training</li>
    </ul>
  </section>

  <section class="service service--support">
    <span class="service-number">4</span>
    <h2 class="service-title">MULTILEVEL SUPPORT</h2>
    <ul class="service-list">
      <li>On-demand Support</li>
      <li>3-Tiered Support</li>
      <li>Remote Support</li>
      <li>Remote Monitoring and Notifications</li>
      <li>IT Management Services</li>
      <li>OEM management</li>
    </ul>
  </section>
</main>
</body>
</html>
```